南谷 睦月というペンネームで活動しているものです。

本業は組織・人財開発領域に特化した支援を行う会社において、
企画の提案、プロジェクトマネジメント、依頼後の進捗管理など、
お客様の中に自身も入りながら、経営を変えていくような支援を行っています。

ご依頼をさせていただく表紙デザインですが、
9月16日にPagoraにて、下記の内容を発行いたしました。
============================
現場を変える人が大切にする4つの視点:
~挑戦した人々の物語から静かに学び取る~

www.bookvale-store.jp/item/Q72KD4MX3N
こちらの内容について、発行に向けた表紙手配が間に合わなかったこともあり、
一旦はデザインを自身で考え、発行をいたしましたが、
表紙は書籍の顔ということもあり、作成依頼を進めることに決めました。

デザイン制作にあたって検討いただきたいのは下記2点です。

検討に当たってのポイントは下記2点です。
① 悩みに対しての答えが見つかるような印象を持てる
② あまり複雑すぎないデザインであること

① 悩みに対しての答えが見つかるような印象を持てる
・取り上げたPagoraでは、スキル・ノウハウ本ではなく、
実践されている方が直面されたエピソードをもとにして、
悩みを解決するためのヒントを取り上げています。
そのようなニュアンスが感じられるようなデザインに期待です。

② あまり複雑なデザインではないこと
・凝ったデザインよりは、わかりやすいデザインを好む方です。
複雑なカラーよりは、色を限りながらも、与えられた題材に対しての
表現を頂けるようなデザインが好みではあります。
※ が、良いものが出てくれば、それ限りではございませんので、
あくまで、現時点の好みとしてお伝えを致します

最終的に今回のコンペでは「R_hoshidaさん」のデザインを採用させて頂きます。
重視した点は改めて、下記の2点がベースとなります。
① 悩みに対しての答えが見つかるような印象を持てる
② あまり複雑なデザインではないこと
絵で①のイメージを喚起しつつ、今回の書籍で押し出していることを文字で強調いただく構成となっており、②の点からも適切と考えて採択をさせて頂きました。

改めて、この度はご提案をいただきましてありがとうございます。

引き続き、個人的な目標としては3か月~6か月に1回の頻度で、
Pagora向けの発行物を執筆していく予定です。
また、このような形でご支援の相談をさせていただきますので、
よろしければ是非、お力添えをどうぞお願い申し上げます。

```html
<!DOCTYPE html>
<html lang="ja">
<head>
<meta charset="utf-8">
<title>現場を変える人が大切にする4つの視点</title>
<link href="https://fonts.googleapis.com/css2?family=Noto+Sans+JP:wght@500;900&family=Noto+Serif+JP:wght@700&family=Noto+Serif:ital@1&display=swap" rel="stylesheet">
<style>
  :root {
    --paper: #ffffff;
    --ink: #111111;
    --accent: #e60012;
    --maze-edge: #fbfbfb;
    --maze-core: #e4e4e4;
    --figure-top: #2a2a2a;
    --figure-bottom: #0d0d0d;
  }
  * { margin: 0; padding: 0; box-sizing: border-box; }
  html, body { width: 750px; height: 1200px; overflow: hidden; background: var(--paper); }
  .cover {
    position: relative;
    width: 750px;
    height: 1200px;
    background: var(--paper);
    overflow: hidden;
  }
  .artwork {
    position: absolute;
    left: 0;
    top: 0;
    width: 750px;
    height: 1200px;
  }
  .title {
    position: absolute;
    left: 28px;
    top: 22px;
    font-family: "Noto Sans JP", sans-serif;
    font-weight: 900;
    font-size: 92px;
    line-height: 96px;
    color: var(--ink);
    letter-spacing: -2px;
  }
  .title span { display: block; }
  .author {
    position: absolute;
    left: 452px;
    top: 4px;
    color: var(--accent);
  }
  .author-name {
    font-family: "Noto Serif JP", serif;
    font-weight: 700;
    font-size: 52px;
    line-height: 62px;
    letter-spacing: 6px;
  }
  .author-roman {
    font-family: "Noto Serif", serif;
    font-style: italic;
    font-size: 17px;
    line-height: 20px;
    color: var(--ink);
    padding-left: 4px;
  }
  .author-rule {
    position: absolute;
    left: 412px;
    top: 98px;
    width: 338px;
    height: 6px;
    background: var(--accent);
  }
  .headline {
    position: absolute;
    left: 40px;
    top: 350px;
    color: var(--accent);
    font-family: "Noto Sans JP", sans-serif;
    font-weight: 900;
  }
  .headline-number {
    position: absolute;
    left: 0;
    top: 0;
    font-size: 270px;
    line-height: 270px;
    letter-spacing: -6px;
  }
  .headline-rest {
    position: absolute;
    left: 180px;
    top: 14px;
    font-size: 96px;
    line-height: 110px;
    white-space: nowrap;
    letter-spacing: -2px;
  }
  .subtitle {
    position: absolute;
    left: 238px;
    top: 508px;
    font-family: "Noto Sans JP", sans-serif;
    font-weight: 500;
    font-size: 40px;
    line-height: 52px;
    color: var(--ink);
  }
  .subtitle span { display: block; }
</style>
</head>
<body>
<main class="cover">
  <svg class="artwork" viewBox="0 0 750 1200">
    <defs>
      <radialGradient id="maze-tone" cx="50%" cy="50%" r="50%">
        <stop offset="0%" style="stop-color: var(--maze-core)"/>
        <stop offset="100%" style="stop-color: var(--maze-edge)"/>
      </radialGradient>
      <linearGradient id="figure-tone" x1="0" y1="0" x2="0" y2="1">
        <stop offset="0%" style="stop-color: var(--figure-top)"/>
        <stop offset="100%" style="stop-color: var(--figure-bottom)"/>
      </linearGradient>
    </defs>

    <g class="maze-area" role="img" aria-label="円形の迷路模様の背景">
      <circle cx="375" cy="920" r="330" fill="url(#maze-tone)"/>
    </g>

    <g class="figure-area" role="img" aria-label="電話をしながら考え込むスーツ姿の男性のシルエット">
      <rect x="240" y="770" width="300" height="460" rx="120" fill="url(#figure-tone)"/>
    </g>

    <g class="alert-icon" role="img" aria-label="注意を示す感嘆符">
      <circle cx="228" cy="752" r="58" fill="var(--accent)"/>
      <rect x="220" y="718" width="16" height="44" rx="7" fill="var(--paper)"/>
      <circle cx="228" cy="780" r="9" fill="var(--paper)"/>
    </g>
  </svg>

  <h1 class="title">
    <span>現場を</span>
    <span>変える人が</span>
    <span>大切にする</span>
  </h1>

  <div class="author">
    <p class="author-name">南谷 睦月</p>
    <p class="author-roman">Minamiya Mutsuki</p>
  </div>
  <div class="author-rule"></div>

  <p class="headline">
    <span class="headline-number">4</span>
    <span class="headline-rest">つの視点</span>
  </p>

  <p class="subtitle">
    <span>挑戦した人々の物語から</span>
    <span>静かに学び取る</span>
  </p>
</main>
</body>
</html>
```